Aged Care Home - TM

We need a website design for a homepage and a content page for an aged care home in Brisbane. I have attached a detailed design/content brief and their logo to be used in concepts. Also bear in mind this design will be skinned for Dot Net Nuke 4.8.2 so design needs to be used on this content management system.

The following elements are required in the design:

• Phone number will be featured in banner on each page 07 5281 6637

• An area for a large flash banner of rotating images on homepage

• Images need to reflect credibility, professionalism and caring (just use some example images for now as we’ll need to source some)

• Large logo in banner as well

• Some icons on homepage to include:

• Download Application Form

• Admission Kit

• Contact Us

```html
<!DOCTYPE html>
<html lang="en">
<head>
<meta charset="utf-8">
<title>Tess Marlow Home – Website Concepts</title>
<link href="https://fonts.googleapis.com/css2?family=Cabin:wght@400;500;600&display=swap" rel="stylesheet">
<style>
  :root {
    --sky: #b3def2;
    --sky-light: #e4f3fa;
    --navy: #1c1c7a;
    --brand-blue: #2a2ab8;
    --green: #7cc300;
    --green-dark: #64a800;
    --green-text: #6cb80a;
    --ink: #1a1a1a;
    --white: #ffffff;
    --placeholder: #c9e7f6;
  }
  * { margin: 0; padding: 0; box-sizing: border-box; }
  html, body { width: 1200px; height: 748px; overflow: hidden; }
  body {
    position: relative;
    font-family: "Cabin", sans-serif;
    color: var(--ink);
    background: linear-gradient(90deg, var(--sky) 0%, var(--sky-light) 25%, var(--sky) 50%, var(--sky-light) 75%, var(--sky) 100%);
  }
  .backdrop-sheet {
    position: absolute; left: 0; top: 500px; width: 600px; height: 248px;
    background: var(--white);
  }
  .page {
    position: absolute; top: 37px; width: 488px;
    background: var(--white);
  }
  .page--home { left: 56px; height: 425px; }
  .page--content { left: 656px; height: 656px; }

  .brand {
    position: absolute; left: 20px; top: 26px;
    display: flex; align-items: center; gap: 8px;
    color: var(--brand-blue); font-size: 13px; font-weight: 400; letter-spacing: 0.2px;
  }
  .brand-dot { width: 10px; height: 10px; border-radius: 50%; background: var(--brand-blue); }
  .call-us {
    position: absolute; right: 20px; top: 22px;
    color: var(--navy); font-size: 9.5px; line-height: 12px; letter-spacing: 0.3px;
  }
  .hero {
    position: absolute; left: 19px; top: 83px; width: 450px; height: 150px;
    background: linear-gradient(90deg, #7a6a4a 0%, #9bbf5a 22%, #4f7a2c 40%, #7fb840 60%, #5c8c30 80%, #a6c25a 100%);
  }
  .main-nav {
    position: absolute; left: 19px; top: 233px; width: 450px; height: 25px;
    background: var(--navy); border-radius: 0 0 9px 9px;
    display: flex; align-items: center; gap: 11px; padding-left: 18px;
  }
  .main-nav span { color: var(--white); font-size: 7.8px; letter-spacing: 0.45px; white-space: nowrap; }

  .action {
    position: absolute; left: 20px; width: 115px; height: 28px;
    background: linear-gradient(180deg, #8bd20a 0%, var(--green) 50%, var(--green-dark) 100%);
    border-radius: 5px;
    color: var(--white); font-size: 7.8px; letter-spacing: 0.4px; line-height: 10px;
    display: flex; align-items: center;
  }
  .action svg { position: absolute; left: 10px; top: 6px; }
  .action-label { width: 100%; text-align: center; padding-left: 22px; }

  .intro {
    position: absolute; left: 153px; top: 272px; width: 318px;
    font-size: 9.4px; line-height: 16.5px; letter-spacing: 0.45px;
  }
  .intro p + p { margin-top: 16.5px; }

  .side-note {
    position: absolute; left: 19px; top: 400px; width: 112px;
    color: var(--navy); font-size: 8.6px; font-weight: 500; line-height: 10.8px; letter-spacing: 0.3px;
  }
  .side-links {
    position: absolute; left: 19px; top: 476px;
    list-style: none; color: var(--green-text); font-size: 7.6px; line-height: 10.5px; letter-spacing: 0.3px;
  }
  .photo-slot {
    position: absolute; left: 19px; top: 549px; width: 115px; height: 75px;
    background: var(--placeholder);
    display: flex; align-items: center; justify-content: center;
    font-size: 8.5px; letter-spacing: 0.3px;
  }

  .content {
    position: absolute; left: 160px; top: 274px; width: 310px;
    font-size: 7.6px; line-height: 10.5px; letter-spacing: 0.3px;
  }
  .content h1 {
    color: var(--green-text); font-size: 11.5px; font-weight: 600; letter-spacing: 1px;
    line-height: 14px; margin-bottom: 7px;
  }
  .content h2 {
    color: var(--navy); font-size: 8.8px; font-weight: 500; letter-spacing: 0.3px; line-height: 10.5px;
  }
  .content section + section { margin-top: 10px; }
</style>
</head>
<body>
  <div class="backdrop-sheet"></div>

  <!-- Homepage -->
  <div class="page page--home">
    <div class="brand"><span class="brand-dot"></span>TESS MARLOW HOME</div>
    <div class="call-us">Call Us Today:<br>07 5281 6637</div>
    <div class="hero" role="img" aria-label="Rotating banner photo: a smiling daughter hugging her elderly mother, and an older couple on a park bench among green trees"></div>
    <nav class="main-nav">
      <span>Home</span><span>About Us</span><span>Accommodation</span><span>Contact Us</span><span>Financial Info</span><span>Philosophy of Care</span><span>Sign up for newsletter</span>
    </nav>

    <div class="action" style="top:277px">
      <svg width="12" height="16" viewBox="0 0 12 16"><rect width="12" height="16" fill="#fff"/><path d="M2 4h8M2 7h8M2 10h8M2 13h8" stroke="#1c1c7a" stroke-width="1"/></svg>
      <span class="action-label">Download<br>Application Form</span>
    </div>
    <div class="action" style="top:316px">
      <svg width="15" height="13" viewBox="0 0 15 13"><path d="M0 1h5l1 1.5h9V13H0z" fill="#fff"/><path d="M0 1h5l1 1.5H0z" fill="#1c1c7a"/></svg>
      <span class="action-label">Admission Kit</span>
    </div>
    <div class="action" style="top:355px">
      <svg width="14" height="16" viewBox="0 0 14 16"><path d="M3 0.5c1 0 2.5 3 2.5 4s-1.5 1.5-1.5 2.5 2.5 5 3.5 5 1.5-1.5 2.5-1.5 3.5 1.5 3.5 2.5-2 3-4 3C5 16 0 8 0 4 0 2 2 0.5 3 0.5z" fill="#fff"/></svg>
      <span class="action-label">Contact Us</span>
    </div>

    <div class="intro">
      <p>We are an Aged Care Facility that has been providing quality care and accommodation to the Brisbane community for over twenty years.</p>
      <p>From this site you can learn more about us, find out all the types of accommodation available, what our Philosophy of Care is, send a message to a resident, contact us to request more information or download a brochure or an application form.</p>
    </div>
  </div>

  <!-- Content page -->
  <div class="page page--content">
    <div class="brand"><span class="brand-dot"></span>TESS MARLOW HOME</div>
    <div class="call-us">Call Us Today:<br>07 5281 6637</div>
    <div class="hero" role="img" aria-label="Banner photo: a smiling daughter hugging her elderly mother, and an older couple on a park bench among green trees"></div>
    <nav class="main-nav">
      <span>Home</span><span>About Us</span><span>Accommodation</span><span>Contact Us</span><span>Financial Info</span><span>Philosophy of Care</span><span>Sign up for newsletter</span>
    </nav>

    <div class="action" style="top:278px">
      <svg width="12" height="16" viewBox="0 0 12 16"><rect width="12" height="16" fill="#fff"/><path d="M2 4h8M2 7h8M2 10h8M2 13h8" stroke="#1c1c7a" stroke-width="1"/></svg>
      <span class="action-label">Download<br>Application Form</span>
    </div>
    <div class="action" style="top:317px">
      <svg width="15" height="13" viewBox="0 0 15 13"><path d="M0 1h5l1 1.5h9V13H0z" fill="#fff"/><path d="M0 1h5l1 1.5H0z" fill="#1c1c7a"/></svg>
      <span class="action-label">Admission Kit</span>
    </div>
    <div class="action" style="top:356px">
      <svg width="14" height="16" viewBox="0 0 14 16"><path d="M3 0.5c1 0 2.5 3 2.5 4s-1.5 1.5-1.5 2.5 2.5 5 3.5 5 1.5-1.5 2.5-1.5 3.5 1.5 3.5 2.5-2 3-4 3C5 16 0 8 0 4 0 2 2 0.5 3 0.5z" fill="#fff"/></svg>
      <span class="action-label">Contact Us</span>
    </div>

    <p class="side-note">We have range of accommodation styles to suit a wide variety of needs. The following types of accommodation are offered;</p>
    <ul class="side-links">
      <li>High Care</li>
      <li>Dementia Specific low Care</li>
      <li>Frail Aged low care</li>
      <li>Hostel low care</li>
      <li>Fee Structure</li>
    </ul>
    <div class="photo-slot" role="img" aria-label="Photo placeholder">photo</div>

    <div class="content">
      <h1>Accommodations</h1>
      <section>
        <h2>Upper Tess Marlow Nursing Suites</h2>
        <p>(High Care)<br>14 beds, 10 single rooms and 2 doubles, dining room, lounge for television or activities. All rooms have reverse cycle air conditioning and bathroom ensuites.</p>
      </section>
      <section>
        <h2>Garden Wing &amp; Hibiscus Wing</h2>
        <p>(Dementia Specific low care).<br>Completely secure area with 35 single rooms with attached bathrooms, an indoor/outdoor garden room for barbeques and activities and a secure garden with walking path, fish pond and bird cage.</p>
      </section>
      <section>
        <h2>Tess Marlow Unit &amp; Kendall Wing</h2>
        <p>(Frail Aged low care)<br>20 single rooms with balconies and bathroom facilities between each room. 18 single rooms with shared bathrooms. All rooms open out onto the garden or courtyard. This area has a dining room and lounge for television or activities.</p>
      </section>
      <section>
        <h2>Ashford, TLC or A&amp;B Wings</h2>
        <p>(Hostel low care)<br>80 single rooms with a bathroom between each room. All rooms have a balcony or open out onto the gardens. This area has communal lounges with televisions. There is a public telephone and a pleasant dining room.<br>Respite accommodation is available for Low Care.<br>All rooms are fully serviced; personal clothing is laundered at the facility, free of charge, unless otherwise requested by relatives.</p>
      </section>
      <section>
        <h2>Fees</h2>
        <p>Our fee structure is based on the national standard. Information on it may be found at; http://www.agedcarefees.example.au/resfees.htm</p>
      </section>
    </div>
  </div>
</body>
</html>
```